Simple, Professional and neat business card design for Vellamor Inc.

We're looking to re-vamp our business card design. We're a supplier of innovative feed ingredients for the North American animal agriculture industry. We are located in Lucknow, Ontario, Canada and our flagship product is a product that prevents milk fever in dairy cows when the calve, it is fed before calving and is very effective compared to other alternatives available on the market today.

Our company has Danish roots and we import all of our product from our Danish partner/manufacturer in Denmark. We like our design to embrace high professionalism while remaining neat and simple.

Target Market(s)

B2B, Feed Mills, Veterinary Clinics, Large integrators/producers,

Industry/Entity Type

Agribusiness

Contact Information for Business Card

We like the rounded corners because they make the card easy to sit in a wallet and not many use it so it makes the card stand out, just possibly something to take account for during the design.

As you can also see on the sliders below, looking for a that simple but proffesional scandinavian design.

Requirements
Nice to have
• Rounded corners
Should not have
• Too vibrant

```html
<!DOCTYPE html>
<html lang="en">
<head>
<meta charset="UTF-8">
<title>Vellamor Inc. – Business Card</title>
<link href="https://fonts.googleapis.com/css2?family=Montserrat:wght@400;600;700;800&display=swap" rel="stylesheet">
<style>
  :root {
    --stage: #161616;
    --card: #2b2b2b;
    --card-edge: #333333;
    --brand-blue: #1479d0;
    --text-light: #e6e6e6;
    --text-muted: #bdbdbd;
    --icon-ring: #8a8a8a;
  }
  * { box-sizing: border-box; margin: 0; padding: 0; }
  html, body {
    width: 1200px; height: 900px; overflow: hidden;
    background: var(--stage);
    font-family: "Montserrat", Arial, sans-serif;
  }
  .stage {
    width: 1200px; height: 900px;
    display: flex; flex-direction: column;
    align-items: center; justify-content: center; gap: 44px;
  }
  .card {
    width: 640px; height: 366px;
    background: var(--card);
    border: 1px solid var(--card-edge);
    border-radius: 26px;
    position: relative;
    box-shadow: 0 14px 34px rgba(0,0,0,.55);
  }
  /* Brand lockup */
  .brand { display: flex; align-items: center; gap: 14px; }
  .brand-dot {
    width: 26px; height: 26px; border-radius: 50%;
    background: var(--brand-blue); flex: none;
  }
  .brand-name {
    font-weight: 800; color: var(--brand-blue);
    letter-spacing: 1px; text-transform: uppercase; line-height: 1;
  }
  /* Front */
  .card-front { display: flex; flex-direction: column; justify-content: center; align-items: center; }
  .card-front .brand-name { font-size: 50px; }
  .tagline {
    margin-top: 18px; font-size: 14px; color: var(--brand-blue);
    letter-spacing: .5px; display: flex; gap: 16px;
  }
  .tagline .sep { color: var(--text-muted); }
  /* Back */
  .card-back {
    padding: 40px 36px;
    display: flex; flex-direction: column; align-items: center;
  }
  .card-back .brand-name { font-size: 38px; }
  .person { text-align: center; margin-top: 20px; }
  .person-name { font-size: 18px; font-weight: 700; color: var(--brand-blue); text-transform: uppercase; letter-spacing: 1px; }
  .person-title { font-size: 12px; font-weight: 600; color: var(--text-light); text-transform: uppercase; letter-spacing: 2px; margin-top: 3px; }
  .person-rule { width: 14px; height: 2px; background: var(--text-light); margin: 8px auto 0; }
  .contact-row {
    display: flex; justify-content: center; gap: 30px;
    font-size: 13px; color: var(--text-light);
  }
  .contact-row:first-of-type { margin-top: 20px; }
  .contact-row + .contact-row { margin-top: 10px; }
  .contact { display: flex; align-items: center; gap: 9px; white-space: nowrap; }
  .contact svg { width: 18px; height: 18px; flex: none; }
  .company-block { margin-top: 16px; font-size: 12.5px; color: var(--text-light); text-align: center; }
  .company-name { font-weight: 700; text-transform: uppercase; letter-spacing: .5px; }
  .company-address { color: var(--text-muted); margin-top: 3px; }
</style>
</head>
<body>
<main class="stage">

  <section class="card card-front">
    <div class="brand">
      <span class="brand-dot"></span>
      <span class="brand-name">Vellamor Inc.</span>
    </div>
    <p class="tagline">
      <span>Preventative Care</span><span class="sep">/</span>
      <span>High-Performance</span><span class="sep">/</span>
      <span>Prescription-Free</span>
    </p>
  </section>

  <section class="card card-back">
    <div class="brand">
      <span class="brand-dot"></span>
      <span class="brand-name">Vellamor Inc.</span>
    </div>
    <div class="person">
      <p class="person-name">Niels Hedegaard</p>
      <p class="person-title">Managing Director</p>
      <div class="person-rule"></div>
    </div>

    <div class="contact-row">
      <div class="contact">
        <svg viewBox="0 0 18 18"><circle cx="9" cy="9" r="8" fill="none" stroke="var(--icon-ring)"/><rect x="6.5" y="4.5" width="5" height="9" rx="1" fill="none" stroke="var(--text-light)"/></svg>
        <span>519-555-0148</span>
      </div>
      <div class="contact">
        <svg viewBox="0 0 18 18"><circle cx="9" cy="9" r="8" fill="none" stroke="var(--icon-ring)"/><rect x="5" y="6" width="8" height="6" rx="1" fill="none" stroke="var(--text-light)"/><line x1="7" y1="9" x2="11" y2="9" stroke="var(--text-light)"/></svg>
        <span>519-555-0172</span>
      </div>
      <div class="contact">
        <svg viewBox="0 0 18 18"><circle cx="9" cy="9" r="8" fill="none" stroke="var(--icon-ring)"/><rect x="5" y="5" width="8" height="8" rx="1" fill="none" stroke="var(--text-light)"/><line x1="5" y1="8" x2="13" y2="8" stroke="var(--text-light)"/></svg>
        <span>519-555-0160</span>
      </div>
    </div>

    <div class="contact-row">
      <div class="contact">
        <svg viewBox="0 0 18 18"><circle cx="9" cy="9" r="8" fill="none" stroke="var(--icon-ring)"/><rect x="4.5" y="6" width="9" height="6" fill="none" stroke="var(--text-light)"/><path d="M4.5 6 L9 9.5 L13.5 6" fill="none" stroke="var(--text-light)"/></svg>
        <span>niels@vellamor.com</span>
      </div>
      <div class="contact">
        <svg viewBox="0 0 18 18"><circle cx="9" cy="9" r="8" fill="none" stroke="var(--icon-ring)"/><path d="M6 5 L8 5 L8.5 7.5 L7.3 8.3 Q8.3 10.3 10 11 L10.7 9.8 L13 10.3 L13 12 Q9 13 6 9 Z" fill="var(--text-light)"/></svg>
        <span>888-555-0193 [toll free]</span>
      </div>
      <div class="contact">
        <svg viewBox="0 0 18 18"><circle cx="9" cy="9" r="8" fill="none" stroke="var(--icon-ring)"/><circle cx="9" cy="9" r="4.5" fill="none" stroke="var(--text-light)"/><line x1="4.5" y1="9" x2="13.5" y2="9" stroke="var(--text-light)"/><ellipse cx="9" cy="9" rx="2" ry="4.5" fill="none" stroke="var(--text-light)"/></svg>
        <span>www.vellamor.com</span>
      </div>
    </div>

    <div class="company-block">
      <p class="company-name">Vellamor Incorporation</p>
      <p class="company-address">Box 417, Brennick, Eastmoor Canada Q4R 7T2</p>
    </div>
  </section>

</main>
</body>
</html>
```